PIKEmoor box Graphic design on existing box dye cut.

we are a flooring company and we are making a sample box. the logo and information that need to be on the box is already established. we just need someone to lay it out on the box "DYE_CUT" . PLEASE CHANGE DASHES ON LOOK TOUCH PICK TO DOTS AND REMOVE THE EXCLAMATION POINT ALSO, please give me a lighter version of the logo...it appears a bit dark on the box. perhaps lighten a bit. .so we need to work with someone who understands how to work with a box dye cut. We want to wrap the logo around the entire 4 sides of the box and leave the top and bottom a black color. The inside of the box will have a similar photo with bullet points (be creative how to include them). I have enclosed a picture of this how it should read. Also, the large inside flap will have a specification sheet. I have included photos of this sheet for your reference… all spec information needs to be included as written. We need to include a QR code on this inside flap which will later allow architects to download the spec.The very front cover that we submitted with the PIKEMOOR look touch pick…I would like a few reeditions of the font on this as I am not completely sold on the font. I am including pictures of how it should look, from a cut and paste model I made.

Target Market(s)

architects and designers

Industry/Entity Type

Architecture

Colors
474747

Requirements
Must have
• Graphic designer MUST know how to work with dye cuts provided and scale artwork to work on dye cut sizes provided. must look professional and elegant this is for architects and designers
Nice to have
• box must look good from all sides . short and long sides. pikemoor photo needs to be on all 4 sides...

```html
<!DOCTYPE html>
<html lang="en">
<head>
<meta charset="utf-8">
<title>PIKEmoor – Cover Font Options</title>
<link rel="stylesheet" href="https://fonts.googleapis.com/css2?family=League+Spartan:wght@800&family=Josefin+Sans:wght@300&family=Marcellus&family=Fondamento:ital@1&family=Racing+Sans+One&family=Macondo+Swash+Caps&family=Questrial&family=Pinyon+Script&display=swap">
<style>
  :root {
    --sheet: #ffffff;
    --ink: #121212;
    --motto-ink: #1e1e1e;
    --wood-light: #d9d9d9;
    --wood-mid: #a9a9a9;
    --wood-dark: #6e6e6e;
    --tagline: #ffffff;
  }
  * { box-sizing: border-box; margin: 0; padding: 0; }
  html, body {
    width: 1200px;
    height: 1200px;
    overflow: hidden;
    background: var(--sheet);
  }
  .option-sheet {
    width: 1200px;
    height: 1200px;
    padding: 12px;
    display: grid;
    grid-template-columns: 1fr 1fr;
    grid-template-rows: repeat(3, 1fr);
    column-gap: 12px;
    row-gap: 8px;
  }
  .cover {
    position: relative;
    overflow: hidden;
  }
  .cover__photo {
    position: absolute;
    inset: 0;
    background:
      radial-gradient(ellipse 18% 30% at 30% 58%, var(--wood-dark), transparent 70%),
      linear-gradient(90deg, var(--wood-light) 0%, var(--wood-mid) 20%, var(--wood-light) 40%, var(--wood-mid) 60%, var(--wood-light) 80%, var(--wood-mid) 100%);
  }
  .cover__title {
    position: absolute;
    top: 30px;
    left: 0;
    width: 100%;
    height: 72px;
    padding-left: 18px;
    display: flex;
    align-items: flex-end;
    justify-content: center;
    color: var(--ink);
    line-height: 1;
    white-space: nowrap;
  }
  .cover__motto {
    position: absolute;
    top: 112px;
    left: 0;
    width: 100%;
    padding-left: 18px;
    text-align: center;
    font-family: "Questrial", sans-serif;
    font-size: 31px;
    letter-spacing: 4px;
    color: var(--motto-ink);
    white-space: nowrap;
  }
  .cover__tagline {
    position: absolute;
    right: 28px;
    bottom: 30px;
    width: 300px;
    padding-bottom: 4px;
    border-bottom: 1.5px solid var(--tagline);
    text-align: right;
    font-family: "Pinyon Script", cursive;
    font-size: 24px;
    color: var(--tagline);
    white-space: nowrap;
  }
  .title--spartan { font-family: "League Spartan", sans-serif; font-weight: 800; font-size: 68px; letter-spacing: 1px; }
  .title--josefin { font-family: "Josefin Sans", sans-serif; font-weight: 300; font-size: 70px; letter-spacing: 1px; }
  .title--marcellus { font-family: "Marcellus", serif; font-size: 66px; font-weight: 700; }
  .title--fondamento { font-family: "Fondamento", cursive; font-style: italic; font-size: 68px; letter-spacing: 2px; }
  .title--racing { font-family: "Racing Sans One", sans-serif; font-size: 64px; font-style: italic; letter-spacing: 1px; }
  .title--macondo { font-family: "Macondo Swash Caps", cursive; font-size: 60px; letter-spacing: 3px; }
</style>
</head>
<body>
  <main class="option-sheet">
    <section class="cover">
      <div class="cover__photo" role="img" aria-label="Grey weathered wood fence with a dog's nose poking through a hole"></div>
      <h2 class="cover__title title--spartan">PIKEMOOR</h2>
      <p class="cover__motto">LOOK • TOUCH • PICK</p>
      <p class="cover__tagline">An Architect's Finest Find</p>
    </section>
    <section class="cover">
      <div class="cover__photo" role="img" aria-label="Grey weathered wood fence with a dog's nose poking through a hole"></div>
      <h2 class="cover__title title--josefin">PIKEMOOR</h2>
      <p class="cover__motto">LOOK • TOUCH • PICK</p>
      <p class="cover__tagline">An Architect's Finest Find</p>
    </section>
    <section class="cover">
      <div class="cover__photo" role="img" aria-label="Grey weathered wood fence with a dog's nose poking through a hole"></div>
      <h2 class="cover__title title--marcellus">PIKEMOOR</h2>
      <p class="cover__motto">LOOK • TOUCH • PICK</p>
      <p class="cover__tagline">An Architect's Finest Find</p>
    </section>
    <section class="cover">
      <div class="cover__photo" role="img" aria-label="Grey weathered wood fence with a dog's nose poking through a hole"></div>
      <h2 class="cover__title title--fondamento">PIKEMOOR</h2>
      <p class="cover__motto">LOOK • TOUCH • PICK</p>
      <p class="cover__tagline">An Architect's Finest Find</p>
    </section>
    <section class="cover">
      <div class="cover__photo" role="img" aria-label="Grey weathered wood fence with a dog's nose poking through a hole"></div>
      <h2 class="cover__title title--racing">PIKEMOOR</h2>
      <p class="cover__motto">LOOK • TOUCH • PICK</p>
      <p class="cover__tagline">An Architect's Finest Find</p>
    </section>
    <section class="cover">
      <div class="cover__photo" role="img" aria-label="Grey weathered wood fence with a dog's nose poking through a hole"></div>
      <h2 class="cover__title title--macondo">PIKEMOOR</h2>
      <p class="cover__motto">LOOK • TOUCH • PICK</p>
      <p class="cover__tagline">An Architect's Finest Find</p>
    </section>
  </main>
</body>
</html>
```